Etiketten für Charity Bier gesucht
Zielgruppe
Wir engagieren uns ehrenamtlich für Kinder in Afrika.
In Einsatz-Teams von freiwilligen Helfern, sammeln wir während 8 Monaten Spendengelder, um Kindern in Townships's Südafrikas eine Zukunft zu bauen, in dem wir nicht staatliche Kindertagesstätten engagierter einheimischer Frauen umbauen.
Vorher bestehen die KITA's nur aus rostigen Wellblechhütten, welche nicht isoliert sind und auf dem KITA Gelände befindet sich weder Rasen, noch ein Spielplatz.
Aufgabenstellung
Um Spenden zu sammeln, möchten wir ein Charity Bier auf den Markt bringen.
Infos zu den Maßen der Etiketten: Sie sollten nicht breiter als 8 cm sein. Wichtig ist, dass sich in der Ecke links oben keine Angaben befinden, da die obere linke Kante schräg nach oben verlaufen wird. Welche Angaben müssen zwingend auf den Etiketten zu finden sein?
Die Promill-Angaben (5.2% VOL)
Inhalts-Angabe (33cl) das Logo des Bierherstellers sollte auch mit auf die Etikette (nicht all zu gross) (siehe Bild Nr.2)
Die Info's zum Bier (Biersorte: Tannfelsbräu ORIGINAL)
Der Name des Bier's sollte Charity Bier sein.
Wir möchten auf der Etikette auch folgendes unbedingt vermerken:
'Diese Flache (Bier) füllt 10 Breischalen für Kinder in Afrika'
Ansonsten haben wir überhaupt keine Vorstellung, was wir wörtlich noch auf die Etikette packen möchten (vielleicht fällt euch ja noch was tolles ein:-)
Was wir uns vom Design her so vorstellen:
Ich habe noch 3 Bilder (siehe Bild 3-4) dazugefügt, mit Designs, welche mir auf Anhieb sehr sehr gut gefallen (damit ihr einen Anhaltspunkt habt:-) Aber ich lasse mich auch gerne von anderen Design-Formen überraschen.

```html
<!DOCTYPE html>
<html lang="de">
<head>
<meta charset="utf-8">
<title>Charity Bier – Etikett</title>
<link rel="stylesheet" href="https://fonts.googleapis.com/css2?family=Ultra&family=Teko:wght@500;600&family=Crimson+Text&display=swap">
<style>
  :root {
    --paper: #ffffff;
    --ink: #0e0e0e;
    --cream: #ffffff;
    --amber: #e8a32b;
    --amber-dark: #2b2b2b;
    --ray: rgba(120, 120, 120, 0.35);
  }
  * { margin: 0; padding: 0; box-sizing: border-box; }
  html, body { width: 848px; height: 1200px; overflow: hidden; background: var(--paper); }
  .canvas { position: relative; width: 848px; height: 1200px; }

  .label { position: absolute; left: 238px; top: 371px; width: 323px; height: 404px; }
  .label-frame { position: absolute; inset: 0; width: 323px; height: 404px; }

  .map-area {
    position: absolute; left: 40px; top: 125px; width: 232px; height: 215px;
    background: radial-gradient(ellipse at 50% 50%, rgba(20,20,20,0.55), rgba(20,20,20,0) 70%);
  }
  .rays { position: absolute; top: 171px; width: 58px; height: 125px; }
  .rays--left { left: 6px; background: linear-gradient(90deg, var(--ray), rgba(120,120,120,0.05)); }
  .rays--right { right: 6px; background: linear-gradient(270deg, var(--ray), rgba(120,120,120,0.05)); }

  .mugs-art {
    position: absolute; left: 83px; top: 28px; width: 158px; height: 52px;
    background: radial-gradient(ellipse at 50% 50%, #f2f2f2 0%, #d8d8d8 45%, rgba(220,220,220,0) 75%);
  }
  .rule { position: absolute; left: 114px; width: 93px; height: 1px; background: var(--cream); opacity: 0.9; }
  .rule--top { top: 89px; }
  .rule--bottom { top: 197px; }

  .title {
    position: absolute; left: 0; width: 100%; text-align: center;
    font-family: 'Ultra', Georgia, serif; color: var(--cream); line-height: 1;
    white-space: nowrap;
  }
  .title--charity { top: 92px; font-size: 45px; letter-spacing: 0.5px; }
  .title--bier { top: 143px; font-size: 45px; letter-spacing: 0.5px; }

  .stars { position: absolute; top: 162px; color: var(--cream); font-size: 11px; letter-spacing: 4px; line-height: 1; }
  .stars--left { left: 44px; }
  .stars--right { left: 236px; }

  .banner { position: absolute; left: 47px; top: 207px; width: 226px; height: 53px; }
  .banner-text {
    position: absolute; left: 68px; top: 216px; width: 184px; text-align: center;
    font-family: 'Teko', 'Arial Narrow', sans-serif; font-weight: 600; font-size: 13px;
    line-height: 17px; color: var(--amber-dark); text-transform: uppercase;
    white-space: nowrap; overflow: hidden;
  }

  .brand {
    position: absolute; left: 100px; top: 356px; width: 123px; text-align: center;
    font-family: 'Teko', 'Arial Narrow', sans-serif; font-weight: 600; font-size: 22px;
    line-height: 1; color: var(--amber);
  }
  .fact {
    position: absolute; top: 370px; font-family: 'Crimson Text', Georgia, serif;
    font-size: 12.5px; color: var(--cream); line-height: 1;
  }
  .fact--volume { left: 31px; }
  .fact--abv { right: 32px; }
</style>
</head>
<body>
<div class="canvas">
  <div class="label">
    <svg class="label-frame" viewBox="0 0 323 404" aria-hidden="true">
      <defs>
        <radialGradient id="labelShade" cx="50%" cy="50%" r="65%">
          <stop offset="0%" stop-color="#3b3d3e"/>
          <stop offset="100%" stop-color="#111213"/>
        </radialGradient>
      </defs>
      <path d="M16,1 H307 A16,16 0 0 0 322,17 V387 A16,16 0 0 0 307,403 H16 A16,16 0 0 0 1,387 V17 A16,16 0 0 0 16,1 Z"
            fill="#ffffff" stroke="#0e0e0e" stroke-width="2"/>
      <path d="M20,6 H303 A14,14 0 0 0 317,20 V384 A14,14 0 0 0 303,398 H20 A14,14 0 0 0 6,384 V20 A14,14 0 0 0 20,6 Z"
            fill="url(#labelShade)" stroke="#0e0e0e" stroke-width="1"/>
    </svg>

    <div class="map-area" role="img" aria-label="Faint silhouette map of Africa"></div>
    <div class="rays rays--left" role="img" aria-label="Sunburst ray decoration"></div>
    <div class="rays rays--right" role="img" aria-label="Sunburst ray decoration"></div>

    <div class="mugs-art" role="img" aria-label="Illustration of two clinking beer mugs with wheat ears"></div>
    <div class="rule rule--top"></div>

    <div class="title title--charity">CHARITY</div>
    <div class="stars stars--left">★★★</div>
    <div class="title title--bier">BIER</div>
    <div class="stars stars--right">★★★</div>
    <div class="rule rule--bottom"></div>

    <svg class="banner" viewBox="0 0 226 53" aria-hidden="true">
      <path d="M16,2 H210 A10,10 0 0 0 218,12 A14,14 0 0 1 218,41 A10,10 0 0 0 210,51 H16 A10,10 0 0 0 8,41 A14,14 0 0 1 8,12 A10,10 0 0 0 16,2 Z"
            fill="#e8a32b" stroke="#2b2b2b" stroke-width="1.5"/>
      <path d="M18,5 H208 V48 H18 Z" fill="none" stroke="#2b2b2b" stroke-width="0.8"/>
      <circle cx="13" cy="26.5" r="3.5" fill="#2b2b2b"/>
      <circle cx="213" cy="26.5" r="3.5" fill="#2b2b2b"/>
    </svg>
    <div class="banner-text">Diese Flasche füllt 10 Jam-<br>breischalen für Kinder in Afrika</div>

    <div class="brand">Tannfelsbräu</div>
    <div class="fact fact--volume">33 cl</div>
    <div class="fact fact--abv">5.2% VOL</div>
  </div>
</div>
</body>
</html>
```